Video production company website

VistaKeel Productions is a video and photography production company serving many Fortune 500 clients traveling to Hawaii and International Destinations. Our primary focus is the Corporate and Incentive group market, and offer both photography and video services. In addition, we also create custom marketing, sales, art, and real estate productions.

Target Market(s)

Corporate Incentive Travel Groups

Industry/Entity Type

Videography

Number of Pages Required

4 page

Requirements
Must have
• see doc with content. This will ultimately be needed to be a wordpress design so we can update ourselves.
Nice to have
• sleek design, professional, cutting edge, modern
Should not have
• too much Hawaii Feel, some ok but we do travel international

```html
<!DOCTYPE html>
<html lang="en">
<head>
<meta charset="utf-8">
<title>VistaKeel Productions — Production</title>
<link rel="stylesheet" href="https://fonts.googleapis.com/css2?family=Lato:wght@300;400;700&family=Playfair+Display:wght@400&display=swap">
<style>
  :root {
    --ink: #ffffff;
    --shade-dark: #0f0f10;
    --shade-mid: #3a3a3b;
    --shade-light: #8a8a8a;
    --accent-red: #e8173f;
    --accent-cyan: #2ee6e0;
    --band-teal: #14b89a;
    --band-yellow: #f2c418;
    --band-red: #e8173f;
    --button-face: #fffdf5;
    --button-ink: #111111;
  }
  * { box-sizing: border-box; margin: 0; padding: 0; }
  html, body { width: 1200px; height: 619px; overflow: hidden; background: var(--shade-dark); }
  body { font-family: "Lato", sans-serif; color: var(--ink); }

  .page { position: relative; width: 1200px; height: 619px; overflow: hidden; }

  .hero-backdrop {
    position: absolute; inset: 0;
    background:
      radial-gradient(ellipse at 62% 30%, rgba(120,120,120,.35), transparent 55%),
      linear-gradient(100deg, var(--shade-dark) 0%, #1c1c1d 35%, var(--shade-mid) 62%, var(--shade-light) 100%);
  }

  .menu-toggle { position: absolute; left: 38px; top: 35px; width: 21px; height: 13px; }

  .page-title {
    position: absolute; left: 84px; top: 62px;
    font-family: "Playfair Display", serif; font-weight: 400;
    font-size: 90px; line-height: 1; letter-spacing: 1px;
    text-shadow: -2px 0 var(--accent-cyan), 2px 0 var(--accent-red);
  }

  .brand-panel { position: absolute; right: 0; top: 0; width: 270px; height: 218px; display: flex; }
  .brand-panel .band-teal { width: 24px; background: var(--band-teal); }
  .brand-panel .band-yellow { width: 32px; background: var(--band-yellow); }
  .brand-panel .band-red { flex: 1; background: var(--band-red); position: relative; }
  .brand-mark {
    position: absolute; left: 12px; top: 30px; width: 190px;
    display: flex; flex-direction: column; align-items: center; gap: 14px;
  }
  .brand-mark .brand-dot { width: 100px; height: 100px; border-radius: 50%; border: 6px solid var(--ink); }
  .brand-mark .brand-name { font-weight: 700; font-size: 14px; letter-spacing: 1px; color: var(--ink); }

  .service { position: absolute; top: 212px; }
  .service-video { left: 86px; }
  .service-photo { left: 623px; }
  .service-icon {
    position: absolute; top: 0; width: 140px; height: 140px; border-radius: 50%;
    border: 2px solid var(--ink);
    box-shadow: -2px 0 var(--accent-cyan), 2px 0 var(--accent-red);
    display: flex; align-items: center; justify-content: center;
  }
  .service-video .service-icon { left: 144px; }
  .service-photo .service-icon { left: 149px; }
  .service-heading {
    position: absolute; top: 178px; white-space: nowrap;
    font-weight: 300; font-size: 44px; letter-spacing: .5px;
    display: flex; align-items: center; gap: 14px;
  }
  .service-video .service-heading { left: 24px; }
  .service-photo .service-heading { left: 23px; }
  .service-heading svg { width: 13px; height: 16px; }
  .service-text {
    position: absolute; top: 248px; width: 460px;
    font-size: 11px; line-height: 18px; text-transform: uppercase; letter-spacing: .1px;
  }

  .action-buttons { position: absolute; left: 902px; top: 542px; display: flex; gap: 14px; }
  .action-button {
    width: 112px; height: 32px; border-radius: 4px; background: var(--button-face);
    color: var(--button-ink); font-size: 11px; font-weight: 700; letter-spacing: .3px;
    display: flex; align-items: center; justify-content: center; text-decoration: none;
    box-shadow: -1px 0 var(--accent-cyan), 2px 0 var(--accent-red);
  }

  .site-footer { position: absolute; left: 22px; top: 576px; font-size: 11px; line-height: 17px; }
  .site-footer .legal-links { display: flex; align-items: center; gap: 8px; }
</style>
</head>
<body>
<div class="page">
  <div class="hero-backdrop" role="img" aria-label="Black and white photo of a smiling passenger in the cockpit of a small seaplane"></div>

  <svg class="menu-toggle" viewBox="0 0 21 13" aria-label="Menu">
    <rect y="0" width="21" height="2" fill="#fff"/>
    <rect y="5.5" width="21" height="2" fill="#fff"/>
    <rect y="11" width="21" height="2" fill="#fff"/>
  </svg>

  <h1 class="page-title">PRODUCTION</h1>

  <div class="brand-panel">
    <div class="band-teal"></div>
    <div class="band-yellow"></div>
    <div class="band-red">
      <div class="brand-mark">
        <span class="brand-dot"></span>
        <span class="brand-name">VISTAKEEL PRODUCTIONS</span>
      </div>
    </div>
  </div>

  <section class="service service-video">
    <div class="service-icon">
      <svg width="84" height="70" viewBox="0 0 84 70" aria-hidden="true">
        <circle cx="16" cy="16" r="13" fill="#fff"/><circle cx="16" cy="16" r="5" fill="#111"/>
        <circle cx="45" cy="16" r="13" fill="#fff"/><circle cx="45" cy="16" r="5" fill="#111"/>
        <rect x="4" y="32" width="54" height="36" rx="4" fill="#fff"/>
        <path d="M60 50 L80 34 L80 68 Z" fill="#fff"/>
      </svg>
    </div>
    <h2 class="service-heading">
      <svg viewBox="0 0 13 16"><path d="M0 0 L13 8 L0 16 Z" fill="#fff"/></svg>VIDEO PRODUCTION
    </h2>
    <p class="service-text">Please contact us for you next project and for a password to watch our sample videos.</p>
  </section>

  <section class="service service-photo">
    <div class="service-icon">
      <svg width="66" height="52" viewBox="0 0 66 52" aria-hidden="true">
        <path d="M4 10 H18 L24 2 H42 L48 10 H62 a4 4 0 0 1 4 4 V48 a4 4 0 0 1 -4 4 H4 a4 4 0 0 1 -4 -4 V14 a4 4 0 0 1 4 -4 Z" fill="#fff"/>
        <circle cx="33" cy="30" r="15" fill="#111"/><circle cx="33" cy="30" r="10" fill="#fff"/>
        <rect x="6" y="14" width="8" height="4" rx="1" fill="#111"/>
      </svg>
    </div>
    <h2 class="service-heading">
      <svg viewBox="0 0 13 16"><path d="M0 0 L13 8 L0 16 Z" fill="#fff"/></svg>PHOTOGRAPHY
    </h2>
    <p class="service-text">Please contact us for a custom quote.&nbsp; Please click here for our gallery.</p>
  </section>

  <nav class="action-buttons">
    <a class="action-button" href="#contact">CONTACT</a>
    <a class="action-button" href="#gallery">GALLERY</a>
  </nav>

  <footer class="site-footer">
    <div class="legal-links">
      <span>•</span>
      <svg width="6" height="8" viewBox="0 0 6 8" aria-hidden="true"><path d="M0 0 L6 4 L0 8 Z" fill="#fff"/></svg>
      <span>T &amp; C / PRIVACY</span>
    </div>
    <div class="copyright">VISTAKEELPRODUCTIONS © 2016. ALL RIGHTS RESERVED.</div>
  </footer>
</div>
</body>
</html>
```